High Quality Business card for Property Management Agency - Super Classy and professional design

High Quality Business card design.

We need a business card designed for our Property Management Agency.
We are located on Sydney's Northern Beaches and manage beautiful properties along the beach and harbor.
We need a design that oozes modern, classy and professional.
I would like it to be double sided with contact details and logo on the front and just the logo on the back.

I need a print ready PDF version of the file as well as an editable photoshop (PSD) version of the file.

Logo and information details attached.

Target Market(s)

Property owners/investors, Male and Female Aged 28-65

Industry/Entity Type

Real Estate

Contact Information for Business Card

Tom Carrick
Tel: 0467 239 018
Email: tom@harvestlaneestates.com.au
Website: www.harvestlaneestates.com.au
Address: Level 2, 17 Wattlecourt Rd, Dunmarra NSW 2187

Font styles to use
Sans Serif

Requirements
Must have
• - Logo front and back
• - Business card details listed above and attached
• - Colour
Nice to have
• Sleek and professional

```html
<!DOCTYPE html>
<html lang="en">
<head>
<meta charset="utf-8">
<title>Harvest Lane Estates – Business Card</title>
<link href="https://fonts.googleapis.com/css2?family=Roboto:wght@400;500;700&display=swap" rel="stylesheet">
<style>
  :root {
    --page-bg: #2b2622;
    --card-black: #0c0c0d;
    --card-charcoal: #1c1d1f;
    --panel-dark: #2a2b2d;
    --panel-mid: #3a3b3e;
    --teal: #3fb8c4;
    --teal-deep: #2a98a4;
    --text-white: #f2f2f2;
    --text-soft: #d6d6d6;
  }
  * { box-sizing: border-box; margin: 0; padding: 0; }
  html, body {
    width: 1200px; height: 858px; overflow: hidden;
    background: var(--page-bg);
    font-family: "Roboto", Arial, sans-serif;
  }
  .sheet {
    width: 1200px; height: 858px;
    display: flex; align-items: center; justify-content: center; gap: 40px;
  }
  .card {
    position: relative; width: 540px; height: 330px; overflow: hidden;
    border-radius: 3px;
    box-shadow: 0 14px 34px rgba(0,0,0,.55);
    background: linear-gradient(135deg, var(--card-charcoal) 0%, var(--card-black) 60%, #050505 100%);
  }
  /* ---------- front ---------- */
  .front-art { position: absolute; inset: 0; width: 100%; height: 100%; }
  .brand-panel-logo {
    position: absolute; left: 18px; top: 0; width: 210px; height: 330px;
    display: flex; align-items: center; justify-content: center;
  }
  .wordmark {
    display: flex; align-items: center; gap: 8px;
    color: var(--text-white); font-weight: 700; text-transform: uppercase;
    letter-spacing: .5px; line-height: 1;
  }
  .wordmark-dot { width: 10px; height: 10px; border-radius: 50%; background: var(--teal); flex: none; }
  .front .wordmark { font-size: 19px; }
  .contact {
    position: absolute; right: 22px; top: 58px; width: 290px;
    color: var(--text-white); text-align: right;
  }
  .contact-name {
    font-size: 22px; font-weight: 400; text-transform: uppercase; letter-spacing: .5px;
    margin-right: 36px; margin-bottom: 12px;
  }
  .contact-row { display: flex; justify-content: flex-end; align-items: flex-start; gap: 12px; margin-bottom: 9px; }
  .contact-text { font-size: 14px; color: var(--text-soft); line-height: 1.3; }
  .contact-icon {
    width: 22px; height: 22px; flex: none; background: var(--teal);
    display: flex; align-items: center; justify-content: center;
  }
  .contact-icon svg { width: 14px; height: 14px; }
  /* ---------- back ---------- */
  .back {
    background: linear-gradient(150deg, #1a1a1b 0%, var(--card-black) 45%, #000 100%);
    display: flex; align-items: center; justify-content: center;
  }
  .back .wordmark { font-size: 34px; gap: 12px; }
  .back .wordmark-dot { width: 16px; height: 16px; }
</style>
</head>
<body>
<main class="sheet">

  <section class="card front" aria-label="Card front">
    <svg class="front-art" viewBox="0 0 540 330" preserveAspectRatio="none" aria-hidden="true">
      <defs>
        <linearGradient id="panelTone" x1="0" y1="0" x2="1" y2="1">
          <stop offset="0" stop-color="#2e2f31"/>
          <stop offset="1" stop-color="#1d1e20"/>
        </linearGradient>
      </defs>
      <polygon points="252,330 300,330 300,290" fill="var(--teal-deep)"/>
      <polygon points="240,330 280,330 300,290 300,270" fill="var(--teal)"/>
      <polygon points="0,0 195,0 262,330 0,330" fill="var(--teal)"/>
      <polygon points="0,0 187,0 252,330 0,330" fill="url(#panelTone)" role="img" aria-label="Fine honeycomb texture in dark charcoal"/>
    </svg>
    <div class="brand-panel-logo">
      <div class="wordmark"><span class="wordmark-dot"></span><span>Harvest Lane Estates</span></div>
    </div>

    <div class="contact">
      <p class="contact-name">Tom Carrick</p>
      <div class="contact-row">
        <span class="contact-text">0467 239 018</span>
        <span class="contact-icon"><svg viewBox="0 0 24 24"><path fill="#0c0c0d" d="M6.6 10.8a15.5 15.5 0 0 0 6.6 6.6l2.2-2.2c.3-.3.7-.4 1-.2 1.1.4 2.3.6 3.6.6.6 0 1 .4 1 1V20c0 .6-.4 1-1 1A17 17 0 0 1 3 4c0-.6.4-1 1-1h3.5c.6 0 1 .4 1 1 0 1.3.2 2.5.6 3.6.1.3 0 .7-.2 1z"/></svg></span>
      </div>
      <div class="contact-row">
        <span class="contact-text">tom@harvestlaneestates.com.au</span>
        <span class="contact-icon"><svg viewBox="0 0 24 24"><path fill="none" stroke="#0c0c0d" stroke-width="2.2" d="M3 6h18v12H3z M3 6l9 7 9-7"/></svg></span>
      </div>
      <div class="contact-row">
        <span class="contact-text">www.harvestlaneestates.com.au</span>
        <span class="contact-icon"><svg viewBox="0 0 24 24"><g fill="none" stroke="#0c0c0d" stroke-width="2"><circle cx="12" cy="12" r="9"/><path d="M3 12h18M12 3c3 3 3 15 0 18M12 3c-3 3-3 15 0 18"/></g></svg></span>
      </div>
      <div class="contact-row">
        <span class="contact-text">Level 2, 17 Wattlecourt Rd, Dunmarra<br>NSW 2187</span>
        <span class="contact-icon"><svg viewBox="0 0 24 24"><path fill="#0c0c0d" d="M12 2a7 7 0 0 0-7 7c0 5 7 13 7 13s7-8 7-13a7 7 0 0 0-7-7zm0 9.5A2.5 2.5 0 1 1 12 6.5a2.5 2.5 0 0 1 0 5z"/></svg></span>
      </div>
    </div>
  </section>

  <section class="card back" aria-label="Card back">
    <div class="wordmark"><span class="wordmark-dot"></span><span>Harvest Lane Estates</span></div>
  </section>

</main>
</body>
</html>
```